Real estate broker business card

Want a modern celan but effective business card for my residential and commercial real estate business. I want the back of the card to advertise my services and to capture business. I have attached the back of my current business card fore ideas
Updates

Target Market(s)

home buyers and seller. commercial buyers and sellers

Industry/Entity Type

Real Estate

Contact Information for Business Card

must have my contact information and my photo

Requirements
Must have
• Lorna Vettridge
• Owner & Qualifying Broker
• Brockhill Real Estate Services
• 555.218.7094
• lorna@brockhillhomes.example
• www.brockhillhomes.example
Nice to have
• metallic
• Business capture text: " Don't buy or lease property without someone looking out for your best interests. I will represent you on your home or investment purchase for FREE!"
• "Home owners, call today to receive a FREE market analysis for your homes value!

```html
<!DOCTYPE html>
<html lang="en">
<head>
<meta charset="utf-8">
<title>Brockhill Real Estate Services — Business Card</title>
<link href="https://fonts.googleapis.com/css2?family=Cinzel:wght@500;600&family=Montserrat:wght@400;500&display=swap" rel="stylesheet">
<style>
  :root {
    --backdrop: #e8e9eb;
    --ink-black: #050505;
    --teal: #1f7f8c;
    --teal-deep: #135e69;
    --silver-light: #f4f4f4;
    --silver-mid: #c9c9c9;
    --silver-dark: #8a8a8a;
    --text-dark: #1c1c1c;
  }
  * { margin: 0; padding: 0; box-sizing: border-box; }
  html, body { width: 1200px; height: 1000px; overflow: hidden; }
  body { background: var(--backdrop); position: relative; font-family: "Montserrat", sans-serif; }

  .card {
    position: absolute; left: 278px; width: 644px; height: 377px; overflow: hidden;
    box-shadow: 4px 6px 8px rgba(0,0,0,0.35);
  }
  .card--front { top: 120px; }
  .card--back { top: 540px; height: 376px; }
  .card__art { position: absolute; inset: 0; width: 100%; height: 100%; }

  .brand-mark {
    position: absolute; border-radius: 50%; background: var(--teal);
  }
  .brand-name {
    position: absolute; font-family: "Cinzel", serif; font-weight: 500;
    color: var(--teal); white-space: nowrap; line-height: 1;
  }

  .card--front .brand-mark { left: 286px; top: 100px; width: 72px; height: 72px; }
  .card--front .brand-name--main { left: 0; width: 644px; text-align: center; top: 196px; font-size: 46px; letter-spacing: 1px; }
  .card--front .brand-name--sub { left: 0; width: 644px; text-align: center; top: 258px; font-size: 15px; letter-spacing: 3px; }

  .card--back .brand-mark { left: 38px; top: 52px; width: 64px; height: 64px; }
  .card--back .brand-name--main { left: 114px; top: 56px; font-size: 34px; letter-spacing: 0.5px; }
  .card--back .brand-name--sub { left: 116px; top: 96px; font-size: 12px; letter-spacing: 2.2px; }

  .agent { position: absolute; left: 62px; top: 168px; }
  .agent__name { font-family: "Cinzel", serif; font-weight: 600; font-size: 29px; color: var(--teal); line-height: 1; }
  .agent__title { font-size: 17px; font-weight: 500; color: var(--text-dark); margin-top: 6px; }

  .contact-list { position: absolute; left: 62px; top: 244px; list-style: none; }
  .contact-list li { display: flex; align-items: center; font-size: 14.5px; color: var(--text-dark); height: 21px; }
  .contact-list svg { width: 16px; height: 16px; margin-right: 8px; flex: none; }

  .agent-photo {
    position: absolute; left: 380px; top: 30px; width: 240px; height: 300px;
    border-radius: 46% 46% 30% 30%;
    background: radial-gradient(ellipse at 50% 35%, #c99a86 0%, #8a5a48 38%, #3b2620 62%, rgba(200,200,200,0) 80%),
                linear-gradient(180deg, rgba(0,0,0,0) 60%, #e9e6e2 85%);
    filter: blur(2px);
  }
</style>
</head>
<body>

<section class="card card--front" aria-label="Card front">
  <svg class="card__art" viewBox="0 0 644 377" preserveAspectRatio="none" aria-hidden="true">
    <defs>
      <linearGradient id="silverFront" x1="0" y1="0" x2="1" y2="1">
        <stop offset="0" stop-color="var(--silver-mid)"/>
        <stop offset="0.35" stop-color="var(--silver-light)"/>
        <stop offset="0.55" stop-color="var(--silver-dark)"/>
        <stop offset="0.75" stop-color="var(--silver-light)"/>
        <stop offset="1" stop-color="var(--silver-mid)"/>
      </linearGradient>
    </defs>
    <rect width="644" height="377" fill="url(#silverFront)"/>
    <path d="M0,120 C120,60 260,52 420,48 C540,45 600,35 644,18 L644,272 C600,318 520,335 380,332 C220,328 90,338 0,356 Z" fill="var(--ink-black)"/>
    <path d="M0,120 C120,60 260,52 420,48 C540,45 600,35 644,18" fill="none" stroke="#ffffff" stroke-width="3" opacity="0.8"/>
    <path d="M0,114 C120,54 260,46 420,42 C540,39 600,29 644,12" fill="none" stroke="#7d7d7d" stroke-width="2"/>
    <path d="M0,356 C90,338 220,328 380,332 C520,335 600,318 644,272" fill="none" stroke="#ffffff" stroke-width="3" opacity="0.85"/>
    <path d="M0,362 C90,344 220,334 380,338 C520,341 600,324 644,278" fill="none" stroke="#7d7d7d" stroke-width="2"/>
  </svg>
  <span class="brand-mark"></span>
  <p class="brand-name brand-name--main">BROCKHILL</p>
  <p class="brand-name brand-name--sub">REAL ESTATE SERVICES</p>
</section>

<section class="card card--back" aria-label="Card back">
  <svg class="card__art" viewBox="0 0 644 376" preserveAspectRatio="none" aria-hidden="true">
    <defs>
      <linearGradient id="silverBack" x1="0" y1="0" x2="1" y2="0.6">
        <stop offset="0" stop-color="var(--silver-mid)"/>
        <stop offset="0.3" stop-color="var(--silver-light)"/>
        <stop offset="0.6" stop-color="#b5b5b5"/>
        <stop offset="0.85" stop-color="var(--silver-light)"/>
        <stop offset="1" stop-color="var(--silver-dark)"/>
      </linearGradient>
      <linearGradient id="silverBand" x1="0" y1="0" x2="1" y2="0">
        <stop offset="0" stop-color="var(--silver-dark)"/>
        <stop offset="0.4" stop-color="var(--silver-light)"/>
        <stop offset="0.7" stop-color="#9c9c9c"/>
        <stop offset="1" stop-color="var(--silver-light)"/>
      </linearGradient>
    </defs>
    <rect width="644" height="376" fill="url(#silverBack)"/>
    <rect width="644" height="134" fill="var(--ink-black)"/>
    <path d="M0,134 L380,134 C470,134 560,136 644,146" fill="none" stroke="#ffffff" stroke-width="2.5"/>
    <path d="M0,376 L0,338 C140,322 320,326 470,318 C560,312 610,296 644,268 L644,376 Z" fill="url(#silverBand)"/>
    <path d="M0,338 C140,322 320,326 470,318 C560,312 610,296 644,268" fill="none" stroke="#5e5e5e" stroke-width="3"/>
    <path d="M0,332 C140,316 320,320 470,312 C560,306 610,290 644,262" fill="none" stroke="#ffffff" stroke-width="2"/>
  </svg>

  <span class="brand-mark"></span>
  <p class="brand-name brand-name--main">BROCKHILL</p>
  <p class="brand-name brand-name--sub">REAL ESTATE SERVICES</p>

  <div class="agent-photo" role="img" aria-label="Portrait photo of the broker, smiling, with long dark hair and a white lace top"></div>

  <div class="agent">
    <h1 class="agent__name">Lorna Vettridge</h1>
    <p class="agent__title">Owner &amp; Qualifying Broker</p>
  </div>

  <ul class="contact-list">
    <li>
      <svg viewBox="0 0 16 16" aria-hidden="true"><circle cx="8" cy="8" r="8" fill="var(--teal)"/><path d="M5.2 4.4l1.4-.3.8 1.9-.9.7c.4.9 1.1 1.6 2 2l.7-.9 1.9.8-.3 1.4c-3 .2-5.8-2.6-5.6-5.6z" fill="#fff"/></svg>
      555.218.7094
    </li>
    <li>
      <svg viewBox="0 0 16 16" aria-hidden="true"><circle cx="8" cy="8" r="8" fill="var(--teal)"/><rect x="4" y="5.2" width="8" height="5.6" fill="#fff"/><path d="M4 5.4l4 3 4-3" fill="none" stroke="var(--teal)" stroke-width="0.9"/></svg>
      lorna@brockhillhomes.example
    </li>
    <li>
      <svg viewBox="0 0 16 16" aria-hidden="true"><circle cx="8" cy="8" r="8" fill="var(--teal)"/><circle cx="8" cy="8" r="3.8" fill="none" stroke="#fff" stroke-width="1"/><path d="M4.2 8h7.6M8 4.2c-1.6 2.2-1.6 5.4 0 7.6M8 4.2c1.6 2.2 1.6 5.4 0 7.6" fill="none" stroke="#fff" stroke-width="0.8"/></svg>
      www.brockhillhomes.example
    </li>
  </ul>
</section>

</body>
</html>
```